Home Health Agency Marketing Portfolio Booklet

We need a 4 page plus cover (total of 8 pages including front and back cover) design of a Home health Agency Marketing Booklet.
We specialize in taking care of homebound senior patients who needs specialize nursing and medical services in the comfort of their homes. We would like to see a design showing the caring and compassionate nature of our agency. The design should show a nice clean modern layout with nice font selection. Attached is a copy of our logo that needs to be use in the brochure. The colors of the logo should be use in the design of the brochure.
The design will consist of the Front and back cover, inside pages of the cover will be blank but there will be folded pockets that will need some design/color. The inside 4 pages will be full cover, double sided and will have all the information of the company.
The Marketing booklet will be 9"x 12".

```html
<!DOCTYPE html>
<html lang="en">
<head>
<meta charset="utf-8">
<title>Bright Haven Home Care – Presentation Folder</title>
<link href="https://fonts.googleapis.com/css2?family=Open+Sans:wght@400;600;700&family=Courgette&display=swap" rel="stylesheet">
<style>
  :root {
    --backdrop: #d4d5d7;
    --brand-blue: #1e9ad6;
    --brand-blue-deep: #1577b4;
    --brand-orange: #f7a533;
    --brand-orange-soft: #fcd79a;
    --white: #ffffff;
    --photo-green: #6f9a48;
    --photo-warm: #d9c9a8;
  }
  * { margin: 0; padding: 0; box-sizing: border-box; }
  html, body { width: 1200px; height: 1004px; overflow: hidden; }
  body {
    background: var(--backdrop);
    font-family: "Open Sans", sans-serif;
    position: relative;
  }
  .panel { position: absolute; top: 62px; width: 485px; height: 644px; overflow: hidden; }
  .panel--back { left: 123px; }
  .panel--front { left: 608px; }
  .panel svg.panel-art { position: absolute; inset: 0; }
  .brand-name {
    position: absolute; left: 30px; top: 32px;
    display: flex; align-items: center; gap: 10px;
    color: var(--brand-blue); font-weight: 700; font-size: 22px; line-height: 1.05;
    letter-spacing: 0.5px;
  }
  .brand-name .dot { width: 34px; height: 34px; border-radius: 50%; background: var(--brand-blue); flex: none; }
  .comfort-badge {
    position: absolute; left: 33px; top: 406px; width: 118px; height: 118px;
    border-radius: 50%; background: var(--white); border: 5px solid #f3eee8;
    display: flex; align-items: center; justify-content: center; text-align: center;
    font-family: "Courgette", cursive; color: var(--brand-blue); font-size: 11.5px; line-height: 1.15;
  }
  .back-footer {
    position: absolute; left: 20px; top: 556px; height: 54px;
    display: flex; align-items: center; color: var(--white);
  }
  .back-footer .footer-brand { font-weight: 700; font-size: 11px; line-height: 1.05; width: 112px; }
  .back-footer .divider { width: 1px; height: 54px; background: rgba(255,255,255,0.7); margin: 0 12px 0 0; }
  .back-footer .details { font-size: 8.6px; line-height: 1.45; padding-right: 10px; }
  .back-footer .details strong { font-weight: 600; }
  .front-cta {
    position: absolute; left: 0; right: 0; top: 496px; text-align: center; color: var(--white);
  }
  .front-cta h2 { font-weight: 600; font-size: 21px; line-height: 30px; letter-spacing: 0.3px; }
  .web-pill {
    display: inline-flex; align-items: center; gap: 6px; margin-top: 14px;
    background: var(--brand-orange); border-radius: 12px; padding: 4px 22px;
    font-size: 10.5px;
  }
  .contact-row { margin-top: 8px; font-size: 10.5px; display: flex; justify-content: center; gap: 12px; }
  .contact-row span { display: inline-flex; align-items: center; gap: 4px; }
  .pockets { position: absolute; inset: 0; pointer-events: none; }
  .pocket-name {
    position: absolute; left: 262px; top: 790px; width: 200px;
    transform: rotate(180deg); text-align: center;
    color: var(--white); font-weight: 700; font-size: 24px; line-height: 1.05;
  }
</style>
</head>
<body>

<!-- Back cover -->
<section class="panel panel--back">
  <svg class="panel-art" width="485" height="644" viewBox="0 0 485 644">
    <defs>
      <linearGradient id="parkTones" x1="0" y1="0" x2="1" y2="1">
        <stop offset="0" stop-color="#b9a24a"/>
        <stop offset="0.5" stop-color="var(--photo-green)"/>
        <stop offset="1" stop-color="#3f6b2e"/>
      </linearGradient>
    </defs>
    <rect width="485" height="520" fill="url(#parkTones)" role="img" aria-label="Photo: caregiver pushing a senior man in a wheelchair through a sunny park"/>
    <path d="M0,0 H330 Q260,150 0,162 Z" fill="var(--white)"/>
    <path d="M330,0 Q260,150 0,162" fill="none" stroke="var(--brand-orange)" stroke-width="5"/>
    <path d="M0,413 Q240,505 485,430 V644 H0 Z" fill="var(--brand-orange)"/>
    <path d="M0,482 Q200,520 485,474" fill="none" stroke="var(--brand-orange-soft)" stroke-width="6"/>
    <path d="M0,490 Q200,528 485,480 V644 H0 Z" fill="var(--brand-blue)"/>
  </svg>
  <div class="brand-name"><span class="dot"></span><span>BRIGHT<br>HAVEN<br>HOME CARE</span></div>
  <div class="comfort-badge">Home health care<br>is being given<br>in the comfort<br>of your home</div>
  <div class="back-footer">
    <div class="footer-brand">BRIGHT HAVEN<br>HOME CARE</div>
    <div class="divider"></div>
    <div class="details"><strong>BRIGHT HAVEN HOME CARE LLC</strong><br>4820 Maple Grove Ave<br>Springfield, MO 65804</div>
    <div class="divider"></div>
    <div class="details">+1-555-210-3398<br>hello@brighthavencare.com<br>www.brighthavenhomecare.com</div>
  </div>
</section>

<!-- Front cover -->
<section class="panel panel--front">
  <svg class="panel-art" width="485" height="644" viewBox="0 0 485 644">
    <defs>
      <linearGradient id="gardenTones" x1="0" y1="0" x2="1" y2="1">
        <stop offset="0" stop-color="#9fae8a"/>
        <stop offset="0.5" stop-color="var(--photo-warm)"/>
        <stop offset="1" stop-color="#3f7fc0"/>
      </linearGradient>
    </defs>
    <rect width="485" height="520" fill="url(#gardenTones)" role="img" aria-label="Photo: smiling senior woman in a wheelchair with a nurse in blue scrubs beside her"/>
    <path d="M0,0 H326 Q250,150 0,162 Z" fill="var(--white)"/>
    <path d="M326,0 Q250,150 0,162" fill="none" stroke="var(--brand-orange)" stroke-width="5"/>
    <path d="M0,420 Q120,470 240,460 Q380,450 485,413 V644 H0 Z" fill="var(--brand-orange)"/>
    <path d="M0,487 Q240,410 485,490 V644 H0 Z" fill="var(--brand-blue)"/>
  </svg>
  <div class="brand-name"><span class="dot"></span><span>BRIGHT<br>HAVEN<br>HOME CARE</span></div>
  <div class="front-cta">
    <h2>A BRIGHT LIFE BEGINS WITH<br>GOOD HEALTH</h2>
    <div class="web-pill">
      <svg width="10" height="10" viewBox="0 0 10 10"><circle cx="5" cy="5" r="4" fill="none" stroke="#fff" stroke-width="1"/><path d="M1,5 H9 M5,1 V9" stroke="#fff" stroke-width="0.8"/></svg>
      www.brighthavenhomecare.com
    </div>
    <div class="contact-row">
      <span><svg width="9" height="9" viewBox="0 0 10 10"><path d="M2,1 L4,1 L5,3.5 L3.8,4.5 Q5,6.5 5.8,6.2 L7,5 L9,6.5 L9,8.5 Q4,9.5 1,3 Z" fill="#fff"/></svg>+1-555-210-3398</span>
      <span><svg width="9" height="9" viewBox="0 0 10 10"><rect x="1.5" y="2" width="7" height="6" rx="1" fill="#fff"/></svg>555-014-2267</span>
    </div>
  </div>
</section>

<!-- Inside pockets -->
<svg class="pockets" width="1200" height="1004" viewBox="0 0 1200 1004">
  <defs>
    <linearGradient id="pocketBlue" x1="0" y1="0" x2="0" y2="1">
      <stop offset="0" stop-color="var(--brand-blue)"/>
      <stop offset="1" stop-color="var(--brand-blue-deep)"/>
    </linearGradient>
  </defs>
  <polygon points="122,706 608,706 597,920 126,920 88,883 88,742" fill="url(#pocketBlue)"/>
  <polygon points="608,706 1093,706 1130,745 1130,879 1098,920 621,920" fill="url(#pocketBlue)"/>
</svg>
<div class="pocket-name">BRIGHT<br>HAVEN<br>HOME CARE</div>

</body>
</html>
```